Granite Path Fitness Presents Harbor Touch Massage with Marguerite

I'm promoting my massage therapy business which is located in a personal one on one training gym. A few of the modalities I offer are:
Basic Relaxation -light or deep.
Medical Massage- specific work for a specific problem.
Reflexology- feet feet and more feet.
Thai Yoga- I stretch you.
Scalp and Feet- Mega tension relief.
For more details, information and to make an appointment call Marguerite at :731 528 4170. E mail: tulipbaker@mailvex.com
I was playing with this: Bring me your tired, aching, stressed-out body and give me a chance to work some magic. (I hate promoting myself and that was extreme for me.)

Target Market(s)

Gym members and walk-ins from the Uptown Kingston, NY neighborhood.

Industry/Entity Type

Business

Colors

Designer to choose colors to be used in the design.

Requirements
Must have
• My name and phone # and my e mail address.
Should not have
• Anything sexual. This is serious healing work done by a licenced professional so there can be no confusion as to intent.

```html
<!DOCTYPE html>
<html lang="en">
<head>
<meta charset="utf-8">
<title>Harbor Touch Massage with Marguerite</title>
<link rel="stylesheet" href="https://fonts.googleapis.com/css2?family=Libre+Baskerville:wght@400;700&family=PT+Sans+Narrow:wght@700&family=Source+Sans+3:wght@400;700&display=swap">
<style>
  :root {
    --ink: #000000;
    --paper: #ffffff;
    --amber: #f2a23a;
    --cocoa: #3b2a1e;
    --signal-red: #e8202a;
    --lemon: #f7ea12;
    --gold: #f2c01e;
    --glow: #fff8ea;
    --umber: #5a3e2b;
  }
  * { margin: 0; padding: 0; box-sizing: border-box; }
  html, body { width: 848px; height: 1200px; overflow: hidden; background: var(--ink); }
  .flyer { position: relative; width: 848px; height: 1200px; background: var(--ink); overflow: hidden; }

  .hero-photo {
    position: absolute; left: 60px; top: 0; width: 720px; height: 700px;
    background:
      radial-gradient(ellipse 190px 150px at 370px 500px, var(--glow) 0%, rgba(255,240,215,.85) 30%, rgba(200,160,120,.35) 65%, rgba(0,0,0,0) 100%),
      radial-gradient(ellipse 360px 340px at 360px 420px, rgba(140,100,70,.75) 0%, rgba(70,45,30,.55) 55%, rgba(0,0,0,0) 100%);
  }

  .headline { position: absolute; left: 0; top: 0; width: 848px; font-family: "Libre Baskerville", serif; }
  .headline span { position: absolute; white-space: nowrap; line-height: 1; }
  .line-intro { left: 112px; top: 84px; font-size: 56px; color: var(--paper); letter-spacing: 1px; }
  .line-tired { left: 154px; top: 140px; font-size: 64px; font-weight: 700; color: var(--amber); }
  .line-stressed { left: 82px; top: 210px; font-size: 64px; font-weight: 700; color: var(--amber); }
  .line-chance { left: 102px; top: 284px; font-size: 44px; font-weight: 700; color: var(--paper); }
  .line-work { left: 196px; top: 332px; font-size: 60px; font-weight: 700; color: var(--paper); word-spacing: 14px; }
  .line-magic { left: 258px; top: 392px; font-size: 136px; font-weight: 700; color: var(--cocoa); }

  .offer-band {
    position: absolute; left: 0; top: 731px; width: 744px; height: 86px;
    background: var(--signal-red); padding: 8px 0 0 33px;
    font-family: "PT Sans Narrow", sans-serif; font-weight: 700; font-size: 31px;
    line-height: 34px; color: var(--paper);
  }

  .modalities { position: absolute; left: 81px; top: 840px; list-style: none;
    font-family: "Source Sans 3", sans-serif; font-size: 24px; color: var(--paper); }
  .modalities li { height: 42.5px; line-height: 36px; }
  .modality-name { color: var(--lemon); font-weight: 700; }

  .contact { position: absolute; left: 0; top: 1084px; width: 848px; text-align: center;
    font-family: "Source Sans 3", sans-serif; }
  .contact-lead { font-size: 12px; color: var(--paper); line-height: 16px; }
  .contact-phone { font-size: 23px; color: var(--gold); line-height: 30px; margin-top: 10px; }
  .contact-email { font-size: 21px; font-weight: 700; color: var(--paper); letter-spacing: 4.6px; line-height: 28px; margin-top: 4px; }
</style>
</head>
<body>
<main class="flyer">
  <div class="hero-photo" role="img" aria-label="Photograph of two cupped open hands holding a bright glowing light against a dark background"></div>

  <h1 class="headline">
    <span class="line-intro">Bring&nbsp; me&nbsp; your</span>
    <span class="line-tired">tired, aching,</span>
    <span class="line-stressed">stressed-out body</span>
    <span class="line-chance">and give me chance to</span>
    <span class="line-work">work some</span>
    <span class="line-magic">magic</span>
  </h1>

  <p class="offer-band">Massage therapy in a personal one on one<br>training gym . A few of the modalities I offer:</p>

  <ul class="modalities">
    <li><span class="modality-name">Basic Relaxation</span> -light or deep.</li>
    <li><span class="modality-name">Medical Massage</span> -specific work for a specific problem.</li>
    <li><span class="modality-name">Reflexology</span> -feet feet and more feet.</li>
    <li><span class="modality-name">Thai Yoga</span> -I stretch you.</li>
    <li><span class="modality-name">Scalp and Feet</span> -Mega tension relief.</li>
  </ul>

  <footer class="contact">
    <p class="contact-lead">information and to make an appointment call</p>
    <p class="contact-phone">Marguerite at :731 528 4170</p>
    <p class="contact-email">E mail: tulipbaker@mailvex.com</p>
  </footer>
</main>
</body>
</html>
```